Copper Lantern Gatherings need a stand out marketing flyer.

Copper Lantern Gatherings is a company that runs empowerment retreats and bespoke corporate training in creating positive change.
We would like an A5 flyer that is 2 sided. the reverse side of the flyer we would like some of our testimonial quotes.

The flyer should be punchy and not too heavy with wordy detail but have enough detail so people can see what we offer. Encouraging people to contact us to find out more

Our empowerment retreats help people to live without limits, be fierce and wild, be creative and courageous, be fearless and free.
Leave behind
- lack of self esteem
- lack of personal power
- lack of focus
- old fears and beliefs
- overwhelm
Find new
- confidence
- personal empowerment
- commitment
- courage
- resilience

Contact details:
website: www.copperlanterngatherings.example.co.uk
email: info@copperlanterngatherings.example.com
Rebecca Thornby Tel: 07700 900 318
Joanna Pelling Tel: 07700 900 752

You can use as much of the detail above in your design as you would like..
I attach our logos. you can pick which ever design you prefer to work with. I have also attached a file that contains the testimonials for the reverse of the slide. I've also attached a few pictures but these aren't necessary in your design they are just an option/idea for you to consider. You can use alternative pictures should you wish to.

Details for our up and coming events can be found on our website

```html
<!DOCTYPE html>
<html lang="en">
<head>
<meta charset="utf-8">
<title>Copper Lantern Gatherings – A5 Flyer</title>
<link rel="stylesheet" href="https://fonts.googleapis.com/css2?family=Ubuntu:ital,wght@0,400;0,500;0,700;1,400&family=Cinzel:wght@600;700&display=swap">
<style>
  :root {
    --stage: #1b3f8b;
    --navy: #14206b;
    --ink: #1b2a6e;
    --royal: #1f4fa6;
    --sky: #2fa3dc;
    --sky-soft: #cfe7f5;
    --pale: #eef1f4;
    --white: #ffffff;
    --quote-grey: #d5d8dc;
  }
  * { box-sizing: border-box; margin: 0; padding: 0; }
  html, body { width: 1200px; height: 931px; overflow: hidden; }
  body {
    background: var(--stage);
    font-family: "Ubuntu", sans-serif;
    position: relative;
  }
  .flyer {
    position: absolute;
    top: 84px;
    width: 540px;
    height: 764px;
    background: var(--pale);
    overflow: hidden;
    box-shadow: 0 18px 40px rgba(0,0,0,.35);
  }
  .flyer--front { left: 40px; }
  .flyer--back { left: 620px; }

  /* ---------- front ---------- */
  .front-hero {
    position: absolute; left: 0; top: 0; width: 100%; height: 300px;
    background: linear-gradient(120deg, #1d3a93 0%, #152a78 35%, #0b0d35 70%, #05061c 100%);
  }
  .front-lower {
    position: absolute; left: 0; top: 250px; width: 100%; height: 450px;
    background: linear-gradient(180deg, #bfe0f4 0%, #e2f1fa 60%, var(--pale) 100%);
    clip-path: polygon(0 12%, 100% 0, 100% 100%, 0 100%);
  }
  .acrostic {
    position: absolute; left: 52px; top: 70px;
    font-family: "Cinzel", serif; font-weight: 700;
    color: #8fc3e8; line-height: 1; font-size: 33px;
  }
  .acrostic span { display: block; height: 32px; }
  .acrostic b { color: #5aa7dc; font-size: 36px; margin-right: 2px; }
  .acrostic-bar {
    position: absolute; left: 48px; top: 64px; width: 30px; height: 138px;
    background: rgba(120,180,225,.35);
  }
  .brand {
    position: absolute; right: 36px; top: 108px; width: 200px; text-align: center;
    font-weight: 500; font-size: 25px; line-height: 1.15; color: #4fa8e6;
  }
  .brand-mark {
    width: 22px; height: 22px; border-radius: 50%; background: #4fa8e6;
    margin: 0 auto 10px;
  }
  .accent-line { position: absolute; height: 4px; background: var(--sky); }
  .offer-box {
    position: absolute; left: 60px; top: 240px; width: 250px; height: 340px;
    background: linear-gradient(160deg, #3bb0e6 0%, #1f7fc6 100%);
    color: var(--white);
    padding: 22px 20px 0 28px;
  }
  .offer-rule { width: 80px; height: 5px; background: var(--white); margin-bottom: 8px; }
  .offer-title { font-weight: 500; font-size: 25px; line-height: 1.2; color: var(--navy); margin-bottom: 6px; }
  .offer-list { list-style: none; font-size: 13.5px; line-height: 1.3; margin-bottom: 14px; }
  .offer-list li::before { content: "• "; }
  .tagline {
    position: absolute; left: 330px; top: 282px; width: 195px;
    font-style: italic; font-size: 13px; color: #44546f; line-height: 1.35;
  }
  .values { position: absolute; left: 330px; top: 330px; list-style: none; }
  .values li {
    display: flex; align-items: flex-start; gap: 8px; white-space: nowrap;
    font-weight: 500; font-size: 18px; color: var(--royal); line-height: 1.1;
    margin-bottom: 8px;
  }
  .values li:nth-child(2) { color: var(--ink); }
  .values svg { flex: none; margin-top: 3px; }
  .front-photo {
    position: absolute; left: 320px; top: 470px; width: 220px; height: 228px;
    background: linear-gradient(120deg, rgba(240,244,248,0) 0%, #e9dccb 45%, #d7a56f 75%, #b9c8d6 100%);
  }
  .contacts { position: absolute; left: 92px; top: 588px; color: var(--navy); }
  .contact-name { font-weight: 500; font-size: 21px; line-height: 1.2; }
  .contact-tel { font-size: 15px; line-height: 1.25; margin-bottom: 5px; }
  .footer-band {
    position: absolute; left: 0; bottom: 0; width: 100%; height: 66px;
    background: linear-gradient(180deg, #3ea9e0 0%, #1e82c8 100%);
    color: var(--white); text-align: center; padding-top: 9px;
  }
  .footer-label { font-weight: 500; font-size: 15px; line-height: 1.2; }
  .footer-line { font-weight: 500; font-size: 12.5px; line-height: 1.3; margin-top: 2px; }

  /* ---------- back ---------- */
  .back-photo {
    position: absolute; left: 0; top: 0; width: 100%; height: 290px;
    background: linear-gradient(90deg, #3b2a6e 0%, #2f4f8c 35%, #2aa7b8 60%, #37b5c2 100%);
  }
  .back-band {
    position: absolute; left: 0; top: 270px; width: 100%; height: 30px;
    background: var(--sky-soft);
  }
  .quote-mark {
    position: absolute; left: 30px; top: 278px;
    font-weight: 700; font-size: 150px;
    color: var(--quote-grey); line-height: 1;
  }
  .testimonials-title {
    position: absolute; left: 0; top: 318px; width: 100%; padding-left: 90px; text-align: center;
    font-weight: 700; font-style: italic; font-size: 26px; color: var(--navy);
  }
  .testimonials {
    position: absolute; left: 40px; top: 364px; width: 460px; list-style: none;
    text-align: center; font-size: 13.5px; line-height: 1.4; color: var(--navy);
  }
  .testimonials li { margin-bottom: 14px; }
</style>
</head>
<body>

<section class="flyer flyer--front" aria-label="Flyer front">
  <div class="front-hero" role="img" aria-label="Dark blue chalkboard texture background"></div>
  <div class="front-lower"></div>

  <div class="acrostic-bar"></div>
  <h1 class="acrostic">
    <span><b>F</b>ace</span>
    <span><b>E</b>verything</span>
    <span><b>A</b>nd</span>
    <span><b>R</b>ise</span>
  </h1>

  <div class="brand">
    <div class="brand-mark"></div>
    Copper Lantern Gatherings
  </div>

  <div class="accent-line" style="left:100px;top:214px;width:190px;"></div>
  <div class="accent-line" style="left:160px;top:226px;width:130px;background:#6cc3ee;"></div>

  <div class="offer-box">
    <div class="offer-rule"></div>
    <h2 class="offer-title">Find new</h2>
    <ul class="offer-list">
      <li>Confidence</li>
      <li>personal empowerment</li>
      <li>commitment</li>
      <li>courage</li>
      <li>resilience</li>
    </ul>
    <div class="offer-rule"></div>
    <h2 class="offer-title">Leave behind</h2>
    <ul class="offer-list">
      <li>lack of self esteem</li>
      <li>lack of personal power</li>
      <li>lack of focus</li>
      <li>old fears and beliefs</li>
      <li>overwhelm</li>
    </ul>
  </div>

  <p class="tagline">Our empowerment retreats help people to live without limits</p>
  <ul class="values">
    <li><svg width="16" height="16" viewBox="0 0 16 16"><rect x="1" y="2" width="12" height="12" fill="none" stroke="#1b2a6e" stroke-width="1.6"/><path d="M4 8l3 3 7-8" fill="none" stroke="#1b2a6e" stroke-width="1.8"/></svg>Be Fierce &amp; Wild</li>
    <li><svg width="16" height="16" viewBox="0 0 16 16"><rect x="1" y="2" width="12" height="12" fill="none" stroke="#1b2a6e" stroke-width="1.6"/><path d="M4 8l3 3 7-8" fill="none" stroke="#1b2a6e" stroke-width="1.8"/></svg>Be Creative &amp;<br>Courageous</li>
    <li><svg width="16" height="16" viewBox="0 0 16 16"><rect x="1" y="2" width="12" height="12" fill="none" stroke="#1b2a6e" stroke-width="1.6"/><path d="M4 8l3 3 7-8" fill="none" stroke="#1b2a6e" stroke-width="1.8"/></svg>Be Fearless &amp; Free</li>
  </ul>

  <div class="front-photo" role="img" aria-label="Photo of a wooden figure sitting beside a large key"></div>

  <div class="contacts">
    <p class="contact-name">Rebecca Thornby</p>
    <p class="contact-tel">07700 900 318</p>
    <p class="contact-name">Joanna Pelling</p>
    <p class="contact-tel">07700 900 752</p>
  </div>

  <footer class="footer-band">
    <p class="footer-label">Contact details:</p>
    <p class="footer-line">www.copperlanterngatherings.example.co.uk |<br>info@copperlanterngatherings.example.com</p>
  </footer>
</section>

<section class="flyer flyer--back" aria-label="Flyer reverse">
  <div class="back-photo" role="img" aria-label="Photo of a wooden figure pulling against strings held by a hand, running toward a flag"></div>
  <div class="back-band"></div>
  <div class="quote-mark" aria-hidden="true">&#8220;</div>
  <h2 class="testimonials-title">Testimonials</h2>
  <ul class="testimonials">
    <li>Do not hesitate, just book it! It will transform and enhance your life.</li>
    <li>If you have a chance to do it then do it, it's one of the best experience of my life.</li>
    <li>The most wonderful weekend of self-discovery and would recommend it to everyone.</li>
    <li>I've met the most amazing people and feel like I am well equipped with the tools now to help myself physically and mentally. The best self-care I've ever invested in.</li>
    <li>It's changed my life, given me perspective and time to develop myself. I've met the most amazing people and learnt so much. It's worth every penny.</li>
    <li>I can't thank Copper Lantern enough for the tools they have metaphorically equipped me with. They are amazing at what they do.</li>
  </ul>
  <footer class="footer-band">
    <p class="footer-label">Contact details:</p>
    <p class="footer-line">www.copperlanterngatherings.example.co.uk |<br>info@copperlanterngatherings.example.com</p>
  </footer>
</section>

</body>
</html>
```